Supplement Rebranding Bottle Design

READ WORD DOCUMENT ATTACHED.
We want to rebrand our current health supplements (see below). We do want it to be modern, vibrant and appealing. Very upscale and elegant as it targets primarily women.
Bottle size: see pictures for bottle size, along with sample bottles that we like; we’re open to any bottle similar to the ones attached.
Current bottles: So ideally, we’d keep the core color on each bottle with a new branding/bottle design. But we're open to your suggestion.

Target Market(s)

mostly women but shouldn't be overly feminine

Requirements
Must have
• see bottle sizes attached

```html
<!DOCTYPE html>
<html lang="en">
<head>
<meta charset="utf-8">
<title>Ava Morrow's Tonic Supplement Labels</title>
<link rel="stylesheet" href="https://fonts.googleapis.com/css2?family=Cinzel:wght@400;600&display=swap">
<style>
  :root {
    --page-bg: #e9e7e4;
    --page-bg-low: #d6d4d1;
    --ink: #ffffff;
    --red-light: #f0643f;
    --red-deep: #d8230f;
    --purple-light: #d07ad3;
    --purple-deep: #9a2fa0;
    --green-light: #4f9a45;
    --green-deep: #1f5a22;
    --blue-light: #3d8fe6;
    --blue-deep: #1553b8;
  }
  * { box-sizing: border-box; margin: 0; padding: 0; }
  html, body { width: 1200px; height: 960px; overflow: hidden; }
  body {
    background: linear-gradient(180deg, var(--page-bg) 0%, var(--page-bg-low) 100%);
    font-family: "Cinzel", serif;
    color: var(--ink);
  }
  .range {
    position: absolute;
    top: 200px;
    left: 40px;
    display: flex;
    gap: 40px;
  }
  .label {
    position: relative;
    width: 250px;
    height: 560px;
    border-radius: 34px;
    overflow: hidden;
  }
  .label__fill { position: absolute; inset: 0; }
  .label--red .label__fill { background: radial-gradient(circle at 60% 40%, var(--red-light), var(--red-deep) 75%); }
  .label--purple .label__fill { background: radial-gradient(circle at 60% 40%, var(--purple-light), var(--purple-deep) 75%); }
  .label--green .label__fill { background: radial-gradient(circle at 60% 40%, var(--green-light), var(--green-deep) 75%); }
  .label--blue .label__fill { background: radial-gradient(circle at 60% 40%, var(--blue-light), var(--blue-deep) 75%); }

  .label__content { position: absolute; inset: 0; padding: 44px 22px 0 26px; }
  .brand-row { display: flex; justify-content: space-between; align-items: center; height: 40px; }
  .brand-name { font-size: 15px; font-weight: 400; letter-spacing: 0.5px; }
  .guarantee-seal {
    width: 36px; height: 36px; border-radius: 50%;
    background: #ffffff;
  }
  .product-name {
    margin-top: 20px;
    font-weight: 600;
    font-size: 40px;
    line-height: 0.95;
    letter-spacing: 0.5px;
  }
  .product-name--wide { font-size: 35px; margin-top: 26px; }
  .product-name--long { font-size: 34px; margin-top: 10px; }
  .product-name sup { font-size: 10px; font-weight: 400; vertical-align: top; }
  .benefit {
    margin-top: 30px;
    font-size: 16px;
    line-height: 1.05;
    letter-spacing: 0.5px;
  }
  .ornament-area {
    position: absolute; right: 10px; top: 300px;
    width: 120px; height: 150px;
    border-radius: 50%;
    background: radial-gradient(circle, rgba(255,255,255,0.16), rgba(255,255,255,0) 70%);
  }
  .supplement-tag {
    position: absolute; left: 26px; top: 456px;
    border: 1px solid var(--ink);
    font-size: 8.5px;
    padding: 1px 4px;
    letter-spacing: 0.3px;
  }
  .count {
    position: absolute; left: 26px; top: 478px;
    display: flex; align-items: center; gap: 6px;
  }
  .count__number { font-size: 34px; font-weight: 400; line-height: 1; }
  .count__unit { font-size: 13px; line-height: 1.05; }
</style>
</head>
<body>
  <main class="range">
    <section class="label label--red">
      <div class="label__fill" role="img" aria-label="Red capsules filling the bottle"></div>
      <div class="ornament-area" role="img" aria-label="Decorative line ornament"></div>
      <div class="label__content">
        <div class="brand-row"><span class="brand-name">Ava Morrow's</span><span class="guarantee-seal"></span></div>
        <h2 class="product-name">Tummy<br>Tonic<sup>TM</sup></h2>
        <p class="benefit">Oxygenating<br>Colon<br>Cleanse</p>
      </div>
      <span class="supplement-tag">Dietary Supplement</span>
      <div class="count"><span class="count__number">90</span><span class="count__unit">Vegetable<br>Capsules</span></div>
    </section>

    <section class="label label--purple">
      <div class="label__fill" role="img" aria-label="Purple capsules filling the bottle"></div>
      <div class="ornament-area" role="img" aria-label="Decorative line ornament"></div>
      <div class="label__content">
        <div class="brand-row"><span class="brand-name">Ava Morrow's</span><span class="guarantee-seal"></span></div>
        <h2 class="product-name">Liver<br>Tonic<sup>TM</sup></h2>
        <p class="benefit">Rejuvenating<br>Cleanse<br>&amp; Detox<br>Formula</p>
      </div>
      <span class="supplement-tag">Dietary Supplement</span>
      <div class="count"><span class="count__number">120</span><span class="count__unit">Vegetable<br>Capsules</span></div>
    </section>

    <section class="label label--green">
      <div class="label__fill" role="img" aria-label="Green capsules filling the bottle"></div>
      <div class="ornament-area" role="img" aria-label="Decorative line ornament"></div>
      <div class="label__content">
        <div class="brand-row"><span class="brand-name">Ava Morrow's</span><span class="guarantee-seal"></span></div>
        <h2 class="product-name product-name--wide">Hormone<br>Tonic<sup>TM</sup></h2>
        <p class="benefit">Supports<br>Healthy<br>Hormone<br>Levels</p>
      </div>
      <span class="supplement-tag">Dietary Supplement</span>
      <div class="count"><span class="count__number">90</span><span class="count__unit">Vegetable<br>Capsules</span></div>
    </section>

    <section class="label label--blue">
      <div class="label__fill" role="img" aria-label="Blue capsules filling the bottle"></div>
      <div class="ornament-area" role="img" aria-label="Decorative line ornament"></div>
      <div class="label__content">
        <div class="brand-row"><span class="brand-name">Ava Morrow's</span><span class="guarantee-seal"></span></div>
        <h2 class="product-name product-name--long">Blood<br>Sugar<br>Tonic<sup>TM</sup></h2>
        <p class="benefit">Supports<br>Healthy<br>Blood<br>Glucose<br>Levels</p>
      </div>
      <span class="supplement-tag">Dietary Supplement</span>
      <div class="count"><span class="count__number">60</span><span class="count__unit">Vegetable<br>Capsules</span></div>
    </section>
  </main>
</body>
</html>
```